Etiketten-Design für Dankeswein
Zielgruppe
Lumora:
Wir stellen für unsere Kunden einen Dankeswein her. Er soll eine Hommage an die Freundschaft und Partnerschaft sein.
Subtitle, could be, but perhaps not:
Under open skies, every story grows.
Name: Lumora (evtl. Änderung auf Kasto)
Aufgabenstellung
Das Ettikett darf auch bunt sein, aber es sollte vorallem sehr Professionell sein.
Der Wein wird rötlich sein, die Flasche weiss durchsichtig. Es werden wahrscheinlich 0,5l Flaschen.
Die Form des Ettikets, kann noch definiert werden.
Es geht um eine Homage an das Treffen von Menschen und die Freundschaft.
Lumora
Hintergrundinfos, die eher für den Hintergrund, Einarbeitung und kleine Abbildung gedacht sind.
FLOVIKA: ist eine IT Firma, die von 2 Partnern gegründet wurde. Das Logo sollte mit drauf, evtl. kann man auch sich an diesen Farben orientieren.
Familie Drommer: Die Tiersymbole repräsentieren die beiden Eltern. Das geschwungene H ist das Familienzeichen. Wenn man es rotiert. ähnelt es wieder einem Schmetterling. Vielleicht kann man da grafisch etwas machen?
Das geschwungene H oder die Tiersymbole haben hohen emotionalen Wert. In dem Wappen ist das neue Familiensymbol eingearbeitet in das noch ältere Familienwappen der Familie. Prio hat das geschwungene H
Für das Ettikett gibt es leider rechtliche Pflichtangaben:
FLOVIKA GmbH
Lindacherstrasse 14 CH-4057 Basel
Erzeugerab füllung:D- RP 7 384 926
A.P.-Nr.7 384 926 XXXX
11,0%vol 50 cl Enthält Sulfite
Deutscher Qualitätswein – Mosel
lumora-wein.example

```html
<!DOCTYPE html>
<html lang="de">
<head>
<meta charset="utf-8">
<title>Lumora – Danke Etikett</title>
<link rel="stylesheet" href="https://fonts.googleapis.com/css2?family=Great+Vibes&family=Raleway:wght@300;400&display=swap">
<style>
  :root {
    --backdrop: #eef0f3;
    --label: #ffffff;
    --frame: #efeee4;
    --script-green: #7aa22a;
    --ghost: rgba(120, 120, 120, 0.08);
    --brand-blue: #3a8fc2;
    --legal-grey: #8c8c8c;
  }
  * { margin: 0; padding: 0; box-sizing: border-box; }
  html, body {
    width: 1200px;
    height: 3017px;
    overflow: hidden;
    background: var(--backdrop);
  }
  .label {
    position: absolute;
    left: 100px;
    top: 850px;
    width: 1000px;
    height: 1316px;
    background: var(--label);
    overflow: hidden;
    box-shadow: 0 6px 30px rgba(0, 0, 0, 0.06);
    font-family: "Raleway", sans-serif;
  }
  .label__frame {
    position: absolute;
    inset: 47px;
    border: 7px solid var(--frame);
  }
  .label__ghost-title {
    position: absolute;
    left: 0;
    right: -220px;
    top: 120px;
    text-align: center;
    font-family: "Great Vibes", cursive;
    font-size: 400px;
    line-height: 1;
    color: var(--ghost);
    white-space: nowrap;
  }
  .label__title {
    position: absolute;
    left: 0;
    right: 0;
    top: 250px;
    text-align: center;
    font-family: "Great Vibes", cursive;
    font-size: 200px;
    line-height: 1;
    color: var(--script-green);
  }
  .label__brand {
    position: absolute;
    left: 0;
    right: 0;
    top: 915px;
    text-align: center;
    font-family: "Raleway", sans-serif;
    font-weight: 400;
    font-size: 44px;
    letter-spacing: 2px;
    color: var(--brand-blue);
  }
  .legal {
    position: absolute;
    left: 0;
    right: 0;
    text-align: center;
    font-weight: 300;
    font-size: 17px;
    line-height: 24px;
    color: var(--legal-grey);
  }
  .legal--address { top: 1006px; }
  .legal--bottling { top: 1064px; }
  .legal--origin { top: 1138px; }
</style>
</head>
<body>
  <main class="label">
    <div class="label__frame"></div>
    <div class="label__ghost-title" aria-hidden="true">Danke</div>
    <h1 class="label__title">Danke</h1>
    <div class="label__brand">FLOVIKA</div>
    <p class="legal legal--address">FLOVIKA GmbH • Lindacherstrasse 14 CH-4057 Basel</p>
    <p class="legal legal--bottling">Erzeugerab füllung:D- RP 7 384 926 • A.P.-Nr.7 384 926 XXXX<br>11,0%vol 50 cl Enthält Sulfite</p>
    <p class="legal legal--origin">Deutscher Qualitätswein – Mosel<br>lumora-wein.example</p>
  </main>
</body>
</html>
```